Card design for orthopaedic surgeons working as The Meridale Orthopaedic Clinic

Business cards, letterhead

Colors

Designer to choose colors to be used in the design.

Requirements
Must have
• Late addition.
• Cards letterhead must have logos of
• Corvane Federated Guild of Surgeons
• Tellmark Orthopaedic Society
Nice to have
• Back of card to have space for appointment time to be added by hand and some blank space for writing incidental other notes.

```html
<!DOCTYPE html>
<html lang="en">
<head>
<meta charset="utf-8">
<title>The Meridale Orthopaedic Clinic – Stationery</title>
<link rel="stylesheet" href="https://fonts.googleapis.com/css2?family=Montserrat:wght@400;500;600&family=Arimo:wght@400;700&display=swap">
<style>
  :root {
    --navy: #0d3350;
    --sky: #5a9fd4;
    --paper: #f6f6f6;
    --backdrop: #e2e2e2;
    --ink: #1e1e1e;
    --rule: #5a9fd4;
    --crest-gold: #c9a35a;
    --crest-red: #b23a32;
    --crest-blue: #6d8bb0;
  }
  * { margin: 0; padding: 0; box-sizing: border-box; }
  html, body { width: 1200px; height: 1200px; overflow: hidden; }
  body {
    background: radial-gradient(circle at 70% 55%, #ececec 0%, var(--backdrop) 70%);
    position: relative;
    font-family: 'Arimo', Arial, sans-serif;
  }
  .sheet, .card {
    position: absolute;
    background: var(--paper);
    box-shadow: 2px 3px 6px rgba(0,0,0,0.35);
    overflow: hidden;
  }
  .abs { position: absolute; }
  .wordmark {
    font-family: 'Montserrat', sans-serif;
    font-weight: 500;
    color: var(--navy);
    white-space: nowrap;
    display: flex;
    align-items: center;
  }
  .wordmark .dot {
    display: inline-block;
    border-radius: 50%;
    background: var(--navy);
  }
  .contact {
    font-family: 'Montserrat', sans-serif;
    color: var(--navy);
    text-align: right;
    white-space: nowrap;
  }
  .contact svg { vertical-align: -1px; margin-left: 3px; }

  /* Letterhead */
  .letterhead { left: 75px; top: 106px; width: 703px; height: 994px; }
  .letterhead .wordmark { left: 50px; top: 80px; font-size: 21px; gap: 8px; }
  .letterhead .wordmark .dot { width: 12px; height: 12px; }
  .letterhead .contact { right: 49px; top: 54px; font-size: 10px; line-height: 12.6px; }
  .letterhead .contact .gap { height: 6px; }
  .letter { left: 50px; width: 604px; font-size: 10px; line-height: 14.2px; color: var(--ink); }
  .letter-date { top: 231px; }
  .letter-recipient { top: 259px; }
  .letter-salutation { top: 358px; font-weight: 700; }
  .letter-body { top: 401px; text-align: justify; }
  .letter-body p { margin-bottom: 14.2px; }
  .letter-closing { top: 713px; }
  .signature { left: 50px; top: 746px; width: 170px; height: 26px; background: linear-gradient(90deg, #c9c9c9, #dcdcdc); border-radius: 3px; }
  .letter-signoff { top: 784px; }
  .crest { background: linear-gradient(180deg, var(--crest-gold), var(--crest-red) 55%, var(--crest-blue)); border-radius: 6px 6px 40% 40%; opacity: 0.85; }
  .badge-plain { background: linear-gradient(180deg, var(--crest-blue), var(--sky)); border-radius: 6px; opacity: 0.8; }
  .letterhead .crest { left: 59px; top: 888px; width: 52px; height: 72px; }
  .letterhead .badge-plain { left: 146px; top: 894px; width: 70px; height: 64px; }
  .wave { left: 0; width: 100%; }
  .letterhead .wave { top: 944px; height: 50px; }
  .web { font-family: 'Montserrat', sans-serif; color: #fff; white-space: nowrap; letter-spacing: 0.2px; }
  .letterhead .web { left: 472px; top: 971px; font-size: 11px; }

  /* Appointment card */
  .appointment { left: 828px; top: 268px; width: 302px; height: 184px; }
  .appointment-title { left: 0; width: 100%; top: 24px; text-align: center; font-family: 'Montserrat', sans-serif; font-weight: 600; font-size: 10px; color: var(--navy); }
  .field-label { left: 22px; font-family: 'Montserrat', sans-serif; font-size: 7.5px; color: var(--navy); }
  .field-rule { left: 50px; width: 230px; height: 0; border-top: 0.8px solid var(--rule); }
  .time-label { left: 187px; font-family: 'Montserrat', sans-serif; font-size: 7.5px; color: var(--navy); }
  .appointment .wordmark { left: 0; width: 100%; justify-content: center; top: 156px; font-size: 9px; gap: 4px; }
  .appointment .wordmark .dot { width: 6px; height: 6px; }

  /* Business card */
  .business { left: 828px; top: 504px; width: 302px; height: 184px; }
  .business .wordmark { left: 20px; top: 33px; font-size: 12px; gap: 5px; }
  .business .wordmark .dot { width: 7px; height: 7px; }
  .person-name { left: 20px; top: 83px; font-family: 'Montserrat', sans-serif; font-weight: 600; font-size: 10px; color: var(--sky); }
  .person-title { left: 20px; top: 96px; font-family: 'Montserrat', sans-serif; font-size: 7.5px; color: var(--navy); }
  .business .contact { right: 19px; top: 112px; font-size: 7.5px; line-height: 9.6px; }
  .business .contact .gap { height: 4px; }
  .business .crest { left: 22px; top: 124px; width: 27px; height: 40px; }
  .business .badge-plain { left: 62px; top: 128px; width: 40px; height: 34px; }
  .business .wave { top: 158px; height: 26px; }
  .business .web { right: 18px; top: 172px; font-size: 7.5px; }
</style>
</head>
<body>

<section class="sheet letterhead">
  <div class="abs wordmark"><span class="dot"></span>The Meridale Orthopaedic Clinic</div>
  <div class="abs contact">
    <div>48 N. W. 5th Street</div>
    <div>Eastvale, Florida, 33190</div>
    <div class="gap"></div>
    <div>(555) 014-2290<svg width="9" height="9" viewBox="0 0 10 10"><path d="M2 0.5 L3.6 2.6 L2.7 3.8 C3.3 5 4.8 6.6 6.2 7.3 L7.4 6.4 L9.5 8 L8.3 9.5 C4.5 9.3 0.7 5.5 0.5 1.7 Z" fill="#5a9fd4"/></svg></div>
    <div>daniel@meridaleortho.com<svg width="9" height="8" viewBox="0 0 10 8"><rect x="0.5" y="0.5" width="9" height="7" fill="none" stroke="#5a9fd4"/><path d="M0.5 0.5 L5 4.5 L9.5 0.5" fill="none" stroke="#5a9fd4"/></svg></div>
  </div>

  <div class="abs letter letter-date">November 12, 2019</div>
  <div class="abs letter letter-recipient">
    Mr. Peter Vance<br>President<br>Halden Group<br>111 Street Name, Suite#<br>City, State, 12345
  </div>
  <div class="abs letter letter-salutation">Dear Mr. Peter,</div>
  <div class="abs letter letter-body">
    <p>Lorem ipsum dolor sit amet, consectetur adipiscing elit. Integer diam quam, egestas eu ultrices eu, suscipit ac sapien. Phasellus eu dui nisi. Nam et euismod diam, nec lobortis tortor. Donec et diam nulla. Aenean varius tincidunt convallis. Aliquam a tortor at lacus dictum aliquet. Nunc laoreet metus sapien, in scelerisque augue consectetur in.</p>
    <p>Fusce nec justo laoreet, egestas justo sed, aliquet sem. Pellentesque pharetra massa non orci bibendum semper. Pellentesque cursus eu lectus a consectetur. Nunc volutpat suscipit posuere. Vestibulum facilisis vel quam malesuada mattis. Nulla in mattis tellus. Maecenas tristique mauris vitae pharetra tincidunt. In ut ornare risus. Integer molestie vestibulum nisi, semper dapibus mi condimentum eu.</p>
    <p>Nullam sagittis elit libero, id fringilla est tincidunt eget. Donec in ipsum ultricies, consectetur quam vel, facilisis elit. Phasellus tincidunt congue risus vel luctus. Suspendisse ut mollis neque. Donec ornare orci in turpis vestibulum, in ultrices metus scelerisque. Pellentesque mattis mattis nunc, nec tincidunt lacus egestas id. Fusce facilisis sagittis neque sit amet vulputate. Aliquam ut eros lobortis tortor facilisis vehicula. Sed sed luctus leo, at laoreet sapien. Donec placerat adipiscing ligula non euismod. In lobortis pretium nisl id luctus.</p>
    <p>Integer gravida tincidunt nibh, scelerisque tincidunt turpis. Suspendisse potenti. Nunc hendrerit euismod lectus id elementum. Fusce vitae gravida velit, quis eleifend lectus. In imperdiet mauris eu dui viverra sagittis. Donec tempor dui diam, condimentum gravida lacus pretium a. Nullam fringilla augue quis arcu placerat scelerisque. Aliquam nec tincidunt augue, sit amet posuere ipsum.</p>
  </div>
  <div class="abs letter letter-closing">Sincerely Yours,</div>
  <div class="abs signature" role="img" aria-label="Handwritten signature of Daniel Harrow"></div>
  <div class="abs letter letter-signoff">Daniel Harrow<br>Managing Director</div>

  <div class="abs crest" role="img" aria-label="Corvane Federated Guild of Surgeons membership badge"></div>
  <div class="abs badge-plain" role="img" aria-label="Tellmark Orthopaedic Society fellowship badge"></div>

  <svg class="abs wave" viewBox="0 0 703 50" preserveAspectRatio="none" aria-hidden="true">
    <path d="M0 10 C220 32 460 -6 703 22 L703 50 L0 50 Z" fill="#5a9fd4"/>
    <path d="M0 22 C230 36 470 6 703 30 L703 50 L0 50 Z" fill="#ffffff"/>
    <path d="M0 24 C230 38 470 8 703 32 L703 50 L0 50 Z" fill="#0d3350"/>
  </svg>
  <div class="abs web">www.meridaleortho.com</div>
</section>

<section class="card appointment">
  <div class="abs appointment-title">Next Appointment</div>
  <div class="abs field-label" style="top:69px">Name</div>
  <div class="abs field-rule" style="top:78px"></div>
  <div class="abs field-label" style="top:96px">Date</div>
  <div class="abs time-label" style="top:96px">Time</div>
  <div class="abs field-rule" style="top:105px"></div>
  <div class="abs field-label" style="top:123px">Note</div>
  <div class="abs field-rule" style="top:132px"></div>
  <div class="abs wordmark"><span class="dot"></span>The Meridale Orthopaedic Clinic</div>
</section>

<section class="card business">
  <div class="abs wordmark"><span class="dot"></span>The Meridale Orthopaedic Clinic</div>
  <div class="abs person-name">Daniel Harrow</div>
  <div class="abs person-title">Managing Director</div>
  <div class="abs contact">
    <div>48 N. W. 5th Street</div>
    <div>Eastvale, Florida, 33190</div>
    <div class="gap"></div>
    <div>(555) 014-2290<svg width="7" height="7" viewBox="0 0 10 10"><path d="M2 0.5 L3.6 2.6 L2.7 3.8 C3.3 5 4.8 6.6 6.2 7.3 L7.4 6.4 L9.5 8 L8.3 9.5 C4.5 9.3 0.7 5.5 0.5 1.7 Z" fill="#5a9fd4"/></svg></div>
    <div>daniel@meridaleortho.com<svg width="7" height="6" viewBox="0 0 10 8"><rect x="0.5" y="0.5" width="9" height="7" fill="none" stroke="#5a9fd4"/><path d="M0.5 0.5 L5 4.5 L9.5 0.5" fill="none" stroke="#5a9fd4"/></svg></div>
  </div>
  <div class="abs crest" role="img" aria-label="Corvane Federated Guild of Surgeons membership badge"></div>
  <div class="abs badge-plain" role="img" aria-label="Tellmark Orthopaedic Society fellowship badge"></div>
  <svg class="abs wave" viewBox="0 0 302 26" preserveAspectRatio="none" aria-hidden="true">
    <path d="M0 2 C90 18 190 -4 302 10 L302 26 L0 26 Z" fill="#5a9fd4"/>
    <path d="M0 10 C95 22 195 2 302 14 L302 26 L0 26 Z" fill="#ffffff"/>
    <path d="M0 11 C95 23 195 3 302 15 L302 26 L0 26 Z" fill="#0d3350"/>
  </svg>
  <div class="abs web">www.meridaleortho.com</div>
</section>

</body>
</html>
```